Tova Brisk Fitness Coaching Project

I am a personal trainer based in London. My services include one-on-one PT sessions, bootcamps.
I would like the design to be minimalistic. With light colours: white, pink, purple.
I specialise in weight loss, flexibility, mobility.

Tova Penrick
Personal Trainer
Email: tova.penrick@mailgrove.net
tel: 07500 918 243
Instagram: Tova Brisk

Target Market(s)

adults, mostly females (age 18-50).

Industry/Entity Type

Fitness

Contact Information for Business Card

Tova Penrick
Personal Trainer
tel: 07500 918 243
Instagram: Tova Brisk

Font styles to use
Serif

Colors
eea4c8
fbd4d5
fdf9cf
cfeae6
cee9f5

Requirements
Nice to have
• minimalistic style
• easy to read and remember

```html
<!DOCTYPE html>
<html lang="en">
<head>
<meta charset="UTF-8">
<title>Tova Brisk Fitness Coaching – Business Card</title>
<link rel="stylesheet" href="https://fonts.googleapis.com/css2?family=Poiret+One&display=swap">
<style>
  :root {
    --page-bg: #bdbdbd;
    --card-bg: #060606;
    --photo-dark: #1b1b1d;
    --photo-mid: #2a2a2c;
    --brand-pink: #ea93c6;
    --brand-pink-soft: #f2b3d6;
  }
  * { margin: 0; padding: 0; box-sizing: border-box; }
  html, body {
    width: 1200px;
    height: 1200px;
    overflow: hidden;
    background: var(--page-bg);
    font-family: "Poiret One", sans-serif;
  }
  .canvas {
    position: relative;
    width: 1200px;
    height: 1200px;
  }
  .card {
    position: absolute;
    left: 380px;
    width: 440px;
    height: 258px;
    background: var(--card-bg);
    overflow: hidden;
  }
  .card--front { top: 240px; }
  .card--back { top: 648px; }

  .card__photo {
    position: absolute;
    inset: 0;
    background: linear-gradient(180deg, var(--photo-mid) 0%, var(--photo-dark) 62%, #241f1c 100%);
  }
  .brand {
    position: absolute;
    left: 0;
    right: 0;
    top: 54px;
    text-align: center;
    color: var(--brand-pink);
  }
  .brand__dot {
    display: block;
    width: 66px;
    height: 66px;
    margin: 0 auto 20px;
    border: 3px solid var(--brand-pink-soft);
    border-radius: 50%;
  }
  .brand__name {
    font-size: 31px;
    letter-spacing: 1px;
    line-height: 1;
  }
  .brand__tagline {
    font-size: 16px;
    letter-spacing: 1px;
    margin-top: 2px;
  }

  .contact {
    position: absolute;
    left: 130px;
    top: 70px;
    color: var(--brand-pink);
  }
  .contact__name {
    font-size: 33px;
    letter-spacing: 1.5px;
    line-height: 1;
    margin-left: 8px;
  }
  .contact__role {
    font-size: 18px;
    letter-spacing: 1.5px;
    margin: 6px 0 8px 28px;
  }
  .contact__list { list-style: none; }
  .contact__item {
    display: flex;
    align-items: center;
    gap: 8px;
    font-size: 14.5px;
    letter-spacing: 0.5px;
    line-height: 18px;
  }
  .contact__icon {
    width: 11px;
    height: 11px;
    flex: none;
  }
</style>
</head>
<body>
<main class="canvas">

  <section class="card card--front">
    <div class="card__photo" role="img" aria-label="Dimmed photo of a woman stretching on a studio floor in front of a white brick wall"></div>
    <div class="brand">
      <span class="brand__dot"></span>
      <div class="brand__name">Tova Brisk</div>
      <div class="brand__tagline">fitness coaching</div>
    </div>
  </section>

  <section class="card card--back">
    <div class="contact">
      <div class="contact__name">Tova Penrick</div>
      <div class="contact__role">Personal Trainer</div>
      <ul class="contact__list">
        <li class="contact__item">
          <svg class="contact__icon" viewBox="0 0 12 12" aria-hidden="true">
            <rect x="0.8" y="2.2" width="10.4" height="7.6" fill="none" stroke="#ea93c6" stroke-width="1.3"/>
            <path d="M1 2.6 L6 6.6 L11 2.6" fill="none" stroke="#ea93c6" stroke-width="1.3"/>
          </svg>
          tova.penrick@mailgrove.net
        </li>
        <li class="contact__item">
          <svg class="contact__icon" viewBox="0 0 12 12" aria-hidden="true">
            <path d="M2.2 1 L4.4 1 L5.2 3.6 L3.8 4.6 C4.5 6 5.9 7.5 7.4 8.2 L8.4 6.8 L11 7.6 L11 9.8 C11 10.5 10.4 11 9.7 11 C5 10.6 1.4 7 1 2.3 C1 1.6 1.5 1 2.2 1 Z" fill="#ea93c6"/>
          </svg>
          07500 918 243
        </li>
        <li class="contact__item">
          <svg class="contact__icon" viewBox="0 0 12 12" aria-hidden="true">
            <circle cx="6" cy="6" r="4.6" fill="none" stroke="#ea93c6" stroke-width="1.5"/>
          </svg>
          Tova Brisk
        </li>
      </ul>
    </div>
  </section>

</main>
</body>
</html>
```